Crestwell Advisory Services

I'm looking to create a flyer for my business to provide a consultant service. I will be providing the following below
Launch Your Business Today for only $150
(state fee not included)
Business Formation includes:
*Limited liability Corporation (LLC)
*Halvers and Quint Number
*FEIN
*Operation Agreement for partnership LLCs (For 2 or more member(s)
*Commercial Activity license (If needed for your Business )
*Same -day turnaround service with documents
Schedule your Appointment today
Call or text:318-472-6051
Email:MoralesCapitalCircle@fernmail.net
Target Market(s)
I want the flyer to attract people who wants to start a business but doesn’t know where to start. I want the flyer to stand out form the other consultant businesses.
Industry/Entity Type
Consultant
Requirements
Must have
- The State fee not included should be in small print
Highlight the price or service
Highlight the phrase "launch you business today"
Nice to have
- Different samples of colors, a variety
Should not have
- should not be all one color

```html
<!DOCTYPE html>
<html lang="en">
<head>
<meta charset="utf-8">
<title>Crestwell Advisory Services – Launch Your Business Today</title>
<link rel="stylesheet" href="https://fonts.googleapis.com/css2?family=Montserrat:wght@500;600;700;800&family=Oswald:wght@600;700&display=swap">
<style>
  :root {
    --orange: #f07122;
    --teal: #00a88f;
    --coral: #ee4a52;
    --white: #ffffff;
    --ink: #1b1b1b;
    --paper: #f4f4f4;
  }
  * { box-sizing: border-box; margin: 0; padding: 0; }
  html, body { width: 960px; height: 1200px; overflow: hidden; background: var(--white); }
  .flyer {
    position: relative;
    width: 960px;
    height: 1200px;
    overflow: hidden;
    font-family: "Montserrat", sans-serif;
    background: linear-gradient(135deg, #ffffff 0%, var(--paper) 60%, #ececec 100%);
  }
  .hero-photo {
    position: absolute;
    left: 0; top: 0;
    width: 960px; height: 500px;
    background:
      radial-gradient(ellipse at 78% 50%, #8fb3dc 0%, #9fbddf 14%, rgba(200,210,222,0) 32%),
      radial-gradient(ellipse at 42% 35%, #f6f6f6 0%, #e4e2e2 40%, rgba(220,218,218,0) 70%),
      linear-gradient(180deg, #bdbbbb 0%, #d9d8d8 50%, #ececec 100%);
  }
  .shapes { position: absolute; left: 0; top: 0; width: 960px; height: 1200px; }
  .headline {
    position: absolute;
    left: 40px; top: 478px;
    width: 880px; height: 80px;
    display: flex; align-items: center; justify-content: center;
    font-family: "Oswald", sans-serif;
    font-weight: 700;
    font-size: 64px;
    line-height: 80px;
    color: var(--white);
    letter-spacing: -0.8px;
    white-space: nowrap;
  }
  .price-box {
    position: absolute;
    left: 83px; top: 565px;
    width: 794px; height: 108px;
    background: var(--white);
    display: flex; align-items: center; justify-content: center;
  }
  .price {
    font-family: "Montserrat", sans-serif;
    font-weight: 800;
    font-size: 84px;
    line-height: 1;
    color: var(--orange);
    letter-spacing: -1px;
  }
  .fine-print {
    position: absolute;
    right: 83px; top: 681px;
    font-size: 13px;
    font-weight: 500;
    color: var(--white);
  }
  .includes-pill {
    position: absolute;
    left: 212px; top: 802px;
    width: 535px; height: 53px;
    border-radius: 27px;
    background: var(--coral);
    color: var(--white);
    font-weight: 700;
    font-size: 25px;
    display: flex; align-items: center; justify-content: center;
  }
  .service-list {
    position: absolute;
    left: 0; top: 870px;
    width: 960px;
    list-style: none;
    text-align: center;
    color: var(--ink);
    font-weight: 500;
    font-size: 21.5px;
  }
  .service-list li { height: 32px; line-height: 32px; }
  .service-list li:nth-child(2) { height: 30px; }
  .service-list li:nth-child(3) { height: 30px; }
  .service-list li:nth-child(4) { height: 34px; }
  .tick {
    display: inline-block;
    width: 18px; height: 18px;
    vertical-align: -2px;
    margin-right: 8px;
  }
  .contact-band {
    position: absolute;
    left: 0; top: 1102px;
    width: 960px; height: 98px;
    background: var(--teal);
  }
  .cta-pill {
    position: absolute;
    left: 184px; top: 1076px;
    width: 665px; height: 54px;
    border-radius: 27px;
    background: var(--orange);
    border: 2px solid rgba(255,255,255,0.85);
    color: var(--white);
    font-weight: 700;
    font-size: 28.5px;
    display: flex; align-items: center; justify-content: center;
  }
  .contact {
    position: absolute;
    top: 1145px;
    height: 28px;
    display: flex; align-items: center;
    color: var(--white);
    font-weight: 700;
    font-size: 23px;
    white-space: nowrap;
  }
  .contact svg { margin-right: 10px; }
  .contact-phone { left: 98px; }
  .contact-email { left: 345px; }
</style>
</head>
<body>
<main class="flyer">
  <div class="hero-photo" role="img" aria-label="Photo of a person in a white shirt about to press a launch button beside a blue toy rocket"></div>

  <svg class="shapes" viewBox="0 0 960 1200" aria-hidden="true">
    <polygon points="0,355 287,442 0,479" fill="var(--teal)"/>
    <polygon points="0,479 960,355 960,805 0,682" fill="var(--orange)"/>
    <polygon points="0,682 582,757 0,807" fill="var(--teal)"/>
  </svg>

  <h1 class="headline">LAUNCH YOUR BUSINESS TODAY</h1>
  <div class="price-box"><p class="price">FOR ONLY $150</p></div>
  <p class="fine-print">(state fee not included)</p>

  <h2 class="includes-pill">Business Formation Includes:</h2>
  <ul class="service-list">
    <li><svg class="tick" viewBox="0 0 18 18"><circle cx="9" cy="9" r="7.8" fill="none" stroke="var(--coral)" stroke-width="1.5"/><path d="M5.5 9.2l2.3 2.3 4.6-4.8" fill="none" stroke="var(--coral)" stroke-width="1.5"/></svg>Limited liability Corporation (LLC)</li>
    <li><svg class="tick" viewBox="0 0 18 18"><circle cx="9" cy="9" r="7.8" fill="none" stroke="var(--coral)" stroke-width="1.5"/><path d="M5.5 9.2l2.3 2.3 4.6-4.8" fill="none" stroke="var(--coral)" stroke-width="1.5"/></svg>Halvers and Quint Number</li>
    <li><svg class="tick" viewBox="0 0 18 18"><circle cx="9" cy="9" r="7.8" fill="none" stroke="var(--coral)" stroke-width="1.5"/><path d="M5.5 9.2l2.3 2.3 4.6-4.8" fill="none" stroke="var(--coral)" stroke-width="1.5"/></svg>FEIN</li>
    <li><svg class="tick" viewBox="0 0 18 18"><circle cx="9" cy="9" r="7.8" fill="none" stroke="var(--coral)" stroke-width="1.5"/><path d="M5.5 9.2l2.3 2.3 4.6-4.8" fill="none" stroke="var(--coral)" stroke-width="1.5"/></svg>Operation Agreement for partnership LLCs (For 2 or more member(s)</li>
    <li><svg class="tick" viewBox="0 0 18 18"><circle cx="9" cy="9" r="7.8" fill="none" stroke="var(--coral)" stroke-width="1.5"/><path d="M5.5 9.2l2.3 2.3 4.6-4.8" fill="none" stroke="var(--coral)" stroke-width="1.5"/></svg>Commercial Activity license (If needed for your Business )</li>
    <li><svg class="tick" viewBox="0 0 18 18"><circle cx="9" cy="9" r="7.8" fill="none" stroke="var(--coral)" stroke-width="1.5"/><path d="M5.5 9.2l2.3 2.3 4.6-4.8" fill="none" stroke="var(--coral)" stroke-width="1.5"/></svg>Same -day turnaround service with documents</li>
  </ul>

  <div class="contact-band"></div>
  <p class="cta-pill">SCHEDULE YOUR APPOINTMENT TODAY</p>

  <p class="contact contact-phone">
    <svg width="26" height="26" viewBox="0 0 26 26" aria-hidden="true"><circle cx="13" cy="13" r="11.5" fill="none" stroke="var(--white)" stroke-width="1.8"/><path d="M9.2 7.2l2 2.6-1.2 1.6c.8 1.8 2.2 3.3 4 4.2l1.6-1.2 2.6 2-1.2 1.8c-4.5-.6-8.2-4.3-8.8-8.8z" fill="none" stroke="var(--white)" stroke-width="1.5" stroke-linejoin="round"/></svg>
    318-472-6051
  </p>
  <p class="contact contact-email">
    <svg width="28" height="20" viewBox="0 0 28 20" aria-hidden="true"><rect x="1" y="2" width="26" height="16" fill="none" stroke="var(--white)" stroke-width="1.6"/><path d="M1 2l13 10 13-10M1 18l10-8M27 18l-10-8" fill="none" stroke="var(--white)" stroke-width="1.6"/></svg>
    MoralesCapitalCircle@fernmail.net
  </p>
</main>
</body>
</html>
```